Pim Tavel Brochure Design

We are a Marketing company offering different services. Services must be outlined on design we will provive text for the services once project is accepted.

Service Titles to include in design

Corporate Branding
Marketing
Web Design 
Business Consultation
Printing
Mailing
Automation
Pim Tavel Choice

Please post designs, we have n

Target Market(s)

18+ Years Old

Must have
• Web 2.0 Graphics
• Eye catching design
Nice to have
• Rich Graphics
• Creativity
Should not have
• Standard Templates
• Only bullets

```html
<!DOCTYPE html>
<html lang="en">
<head>
<meta charset="utf-8">
<title>Pim Tavel Marketing – Services</title>
<link rel="stylesheet" href="https://fonts.googleapis.com/css2?family=Open+Sans:ital,wght@0,600;0,700;1,700&display=swap">
<style>
  :root {
    --orange-core: #e99d22;
    --orange-mid: #ec7a14;
    --orange-edge: #ef5206;
    --orange-deep: #d84300;
    --paper: #ffffff;
    --ink-light: #ffffff;
    --arrow-grey: #9a9a9a;
    --brand-orange: #f4a11c;
  }
  html, body {
    margin: 0;
    padding: 0;
    overflow: hidden;
    background: var(--paper);
  }
  .brochure {
    width: 850px;
    height: 1200px;
    position: relative;
    overflow: hidden;
    background: var(--paper);
  }
  .brochure svg { display: block; }
  .service-title {
    font-family: "Open Sans", Arial, sans-serif;
    font-weight: 700;
    font-style: italic;
    font-size: 25px;
    fill: var(--ink-light);
  }
  .page-heading {
    font-family: "Open Sans", Arial, sans-serif;
    font-weight: 600;
    font-size: 60px;
    fill: var(--ink-light);
    letter-spacing: -0.5px;
  }
  .brand-name {
    font-family: "Open Sans", Arial, sans-serif;
    font-weight: 700;
    font-size: 18px;
    fill: var(--brand-orange);
  }
  .ring { fill: none; stroke: var(--ink-light); stroke-width: 0.8; opacity: 0.95; }
  .arrow-outline { fill: none; stroke: var(--ink-light); stroke-width: 0.9; }
  .arrow-outline--grey { stroke: var(--arrow-grey); }
  .glow-band { fill: #ffffff; opacity: 0.08; }
</style>
</head>
<body>
<main class="brochure">
<svg width="850" height="1200" viewBox="0 0 850 1200" xmlns="http://www.w3.org/2000/svg">
  <defs>
    <radialGradient id="top-fill" cx="0.45" cy="0.55" r="0.75">
      <stop offset="0" stop-color="var(--orange-core)"/>
      <stop offset="0.55" stop-color="var(--orange-mid)"/>
      <stop offset="1" stop-color="var(--orange-edge)"/>
    </radialGradient>
    <radialGradient id="bottom-fill" cx="0.45" cy="0.48" r="0.72">
      <stop offset="0" stop-color="var(--orange-core)"/>
      <stop offset="0.55" stop-color="var(--orange-mid)"/>
      <stop offset="1" stop-color="var(--orange-edge)"/>
    </radialGradient>
    <linearGradient id="figure-fill" x1="0" y1="0" x2="0" y2="1">
      <stop offset="0" stop-color="#f4a468" stop-opacity="0.75"/>
      <stop offset="1" stop-color="#f0a060" stop-opacity="0.5"/>
    </linearGradient>
    <clipPath id="top-panel-clip">
      <path d="M0,0 H850 V486 C740,492 660,532 565,539 L282,539 C180,539 110,592 0,592 Z"/>
    </clipPath>
    <clipPath id="bottom-panel-clip">
      <path d="M0,662 C110,662 200,607 285,607 C380,607 470,662 565,662 C680,662 760,607 850,607 V1200 H0 Z"/>
    </clipPath>
  </defs>

  <!-- top panel -->
  <g class="panel panel--top">
    <path fill="var(--orange-deep)" d="M0,0 H850 V494 C740,500 660,540 565,547 L282,547 C180,547 110,600 0,600 Z"/>
    <path fill="url(#top-fill)" d="M0,0 H850 V486 C740,492 660,532 565,539 L282,539 C180,539 110,592 0,592 Z"/>
    <g clip-path="url(#top-panel-clip)">
      <path class="glow-band" d="M0,257 C90,257 200,310 285,314 L565,314 C680,314 760,262 850,257 V600 H0 Z"/>
      <g class="rings rings--top-left">
        <circle class="ring" cx="47" cy="115" r="127"/>
        <circle class="ring" cx="47" cy="115" r="137"/>
        <circle class="ring" cx="47" cy="115" r="184"/>
        <circle class="ring" cx="47" cy="115" r="197"/>
      </g>
      <rect class="figure-placeholder" role="img" aria-label="Faint silhouette of a businessman walking with a briefcase"
            x="570" y="72" width="94" height="365" rx="22" fill="url(#figure-fill)"/>
      <g class="rings rings--top-right">
        <circle class="ring" cx="784" cy="256" r="125"/>
        <circle class="ring" cx="784" cy="256" r="135"/>
        <circle class="ring" cx="784" cy="256" r="183"/>
        <circle class="ring" cx="784" cy="256" r="197"/>
      </g>
    </g>
    <path class="arrow-outline" d="M245,278 L222,257 L227,252 L212,250 L214,264 L219,260 L242,281 Z"/>
    <text class="service-title" x="270" y="65" text-anchor="end">Automation</text>
    <text class="service-title" x="270" y="322" text-anchor="end">Pim Tavel Choice</text>
    <text class="page-heading" x="619" y="301">Services</text>
  </g>

  <!-- brand strip -->
  <g class="brand">
    <circle cx="637" cy="558" r="10" fill="var(--brand-orange)"/>
    <text class="brand-name" x="654" y="565">Pim Tavel Marketing</text>
  </g>
  <path class="arrow-outline arrow-outline--grey" d="M16,626 H48 L41,617 H46 L60,629 L46,641 H41 L48,632 H16 Z"/>

  <!-- bottom panel -->
  <g class="panel panel--bottom">
    <path fill="var(--orange-deep)" d="M0,662 C110,662 200,607 285,607 C380,607 470,662 565,662 C680,662 760,607 850,607 V1200 H0 Z"/>
    <path fill="url(#bottom-fill)" d="M0,678 C110,678 200,623 285,623 C380,623 470,678 565,678 C680,678 760,623 850,623 V1200 H0 Z"/>
    <g clip-path="url(#bottom-panel-clip)">
      <path class="glow-band" d="M0,947 L40,947 C120,940 200,918 285,918 C400,918 480,947 600,947 C700,940 780,920 850,918 V1200 H0 Z"/>
      <g class="rings rings--center">
        <circle class="ring" cx="411" cy="665" r="126"/>
        <circle class="ring" cx="411" cy="665" r="136"/>
        <circle class="ring" cx="411" cy="665" r="183"/>
        <circle class="ring" cx="411" cy="665" r="198"/>
      </g>
      <g class="rings rings--bottom-right">
        <circle class="ring" cx="784" cy="1141" r="133"/>
        <circle class="ring" cx="784" cy="1141" r="144"/>
        <circle class="ring" cx="784" cy="1141" r="205"/>
        <circle class="ring" cx="784" cy="1141" r="225"/>
      </g>
      <g class="rings rings--bottom-left">
        <circle class="ring" cx="0" cy="1204" r="126"/>
        <circle class="ring" cx="0" cy="1204" r="139"/>
        <circle class="ring" cx="0" cy="1204" r="173"/>
        <circle class="ring" cx="0" cy="1204" r="187"/>
      </g>
    </g>
    <path class="arrow-outline" d="M238,855 L258,830 L253,829 L268,823 L267,838 L263,834 L242,858 Z"/>
    <path class="arrow-outline" d="M599,928 L620,952 L622,947 L631,960 L616,959 L619,955 L602,926 Z"/>
    <path class="arrow-outline" d="M221,1090 L194,1103 L196,1098 L181,1107 L195,1115 L194,1110 L223,1096 Z"/>

    <text class="service-title" x="270" y="692" text-anchor="end">Corporate Branding</text>
    <text class="service-title" x="299" y="692">Web Design</text>
    <text class="service-title" x="834" y="692" text-anchor="end">Printing</text>
    <text class="service-title" x="270" y="975" text-anchor="end">Marketing</text>
    <text class="service-title" x="299" y="975">Business Consultation</text>
    <text class="service-title" x="834" y="975" text-anchor="end">Mailing</text>
  </g>
</svg>
</main>
</body>
</html>
```